Harbison Projects Promo Brochure

Design a simple ,visually impactful brochure that will articulate our company experience and services to prospective clients.

We need to project to have the following elements / structure:
1. Company Intro
2. Company Services
3. Experience
4. Contact Info
5. Images

I'd like to use icons and imagery as needed to illustrate services and experience.
This brochure will be emailed, so the final version will need to be compressed.

I've uploaded our Owner Rep Services, which has phasing, and services (within each phase), see attached. This info needs to be cleanly added to a brochure.

The "Why Harbison Building Management" doc, copy, needs to be included in the brochure.

Include contact info:
Harbison Projects Services, LLC
214-555-0193
www.harbisonprojgroup.example

Target Market(s)

Restaurants and Hospitality Concepts

Font styles to use
Sans Serif

Colors

Designer to choose colors to be used in the design.

Requirements
Must have
• Very easy to read. Clean.
Information and images should be balanced nicely on the page.

use colors of our logo: red, black, grey, white
Should not have
• Very busy text or images.

```html
<!DOCTYPE html>
<html lang="en">
<head>
<meta charset="utf-8">
<title>Harbison Projects Brochure</title>
<link href="https://fonts.googleapis.com/css2?family=Open+Sans:wght@400;600;700;800&display=swap" rel="stylesheet">
<style>
  :root{
    --stage:#e4e4e4;
    --navy:#122266;
    --navy-deep:#0b1233;
    --maroon:#5b1620;
    --red:#e3262b;
    --red-soft:#b8242f;
    --ink:#1a1a1a;
    --grey:#7a7a7a;
    --grey-light:#c9c9c9;
    --white:#ffffff;
  }
  *{box-sizing:border-box;margin:0;padding:0}
  html,body{width:965px;height:1200px;overflow:hidden;background:var(--stage);font-family:"Open Sans",Arial,sans-serif}
  .spread{position:absolute;top:391px;left:20px;display:flex;gap:20px}
  .page{position:relative;width:295px;height:418px;overflow:hidden;background:var(--white);box-shadow:0 2px 6px rgba(0,0,0,.15)}
  .page-art{position:absolute;inset:0;width:100%;height:100%}
  .abs{position:absolute}

  /* cover */
  .cover{background:var(--navy)}
  .brand{left:0;width:100%;text-align:center;color:var(--white)}
  .brand-mark{display:block;margin:0 auto 6px;width:34px;height:34px;background:var(--red)}
  .brand-name{font-weight:800;font-size:7.5px;letter-spacing:.2px}
  .cover .brand{top:50px}
  .cover-lead{left:0;width:100%;text-align:center;color:var(--white);font-weight:700;font-size:11px;line-height:15.5px;top:136px}
  .cover-title{left:0;width:100%;text-align:center;color:var(--red);font-weight:800;font-size:23px;top:164px;letter-spacing:.2px}
  .cover-sub{left:0;width:100%;text-align:center;color:var(--red);font-weight:700;font-size:13.2px;top:194px}
  .cover-web{left:0;width:100%;text-align:center;color:var(--ink);font-weight:700;font-size:6.4px;letter-spacing:2.6px;bottom:7px}

  /* why page */
  .why-head{left:14px;top:15px;color:var(--ink);font-size:13px;line-height:14.5px}
  .why-head strong{display:block;color:var(--red);font-weight:700}
  .why-rule{left:79px;top:67px;width:94px;height:1.5px;background:var(--red)}
  .why-rule::after{content:"";position:absolute;right:-2px;top:-1.5px;width:4px;height:4px;background:var(--red)}
  .point{width:130px}
  .point h3{color:var(--red);font-size:7.4px;font-weight:700;margin-bottom:3px;display:flex;align-items:center;gap:4px}
  .point h3::before{content:"";width:5px;height:5px;background:var(--ink);border-radius:50%}
  .point p{font-size:4.6px;line-height:6.6px;color:var(--ink);margin-bottom:2px}
  .point p.note{padding-left:4px}
  .point .mark{color:var(--red)}

  /* contact */
  .contact{background:var(--maroon)}
  .contact-title{left:0;width:100%;text-align:center;color:var(--white);font-weight:700;font-size:19px;top:88px}
  .contact-line{left:0;width:100%;display:flex;justify-content:center;align-items:center;gap:8px;color:var(--white);font-size:9.6px}
  .contact-line svg{width:10px;height:10px;flex:none}
  .contact .brand{top:330px;left:16px;width:100px}
  .follow{right:16px;top:388px;color:var(--white);font-size:9.5px;display:flex;align-items:center;gap:4px}
  .follow span.dot{width:11px;height:11px;border:1.3px solid var(--white);border-radius:50%}
</style>
</head>
<body>
<main class="spread">

  <!-- Cover -->
  <section class="page cover">
    <svg class="page-art" viewBox="0 0 438 620" preserveAspectRatio="none" aria-hidden="true">
      <defs>
        <linearGradient id="coverSky" x1="0" y1="0" x2="1" y2="1">
          <stop offset="0" stop-color="#0b1233"/><stop offset="1" stop-color="#14287a"/>
        </linearGradient>
        <linearGradient id="coverPhoto" x1="0" y1="0" x2="1" y2="1">
          <stop offset="0" stop-color="#3c4a6e"/><stop offset=".45" stop-color="#d9d9d6"/><stop offset=".8" stop-color="#a33a33"/><stop offset="1" stop-color="#5a4a44"/>
        </linearGradient>
      </defs>
      <rect width="438" height="620" fill="url(#coverSky)"/>
      <polygon points="0,0 345,0 0,250" fill="#5b1620"/>
      <polygon points="345,0 438,0 438,60 250,340 150,330" fill="#0b1233" opacity=".55"/>
      <polygon points="0,95 0,300 70,245" fill="#b8242f"/>
      <polygon points="0,250 110,170 250,300 0,300" fill="#122266" opacity=".6"/>
      <path d="M260 300 Q330 250 438 280 L438 420 Q350 380 260 360Z" fill="#0b1233" opacity=".5"/>
      <polygon points="0,380 438,470 438,620 0,620" fill="url(#coverPhoto)" role="img" aria-label="Photo of a restaurant building with angled gables and lit sign letters at dusk"/>
    </svg>
    <div class="abs brand"><span class="brand-mark"></span><span class="brand-name">HARBISON PROJECTS</span></div>
    <p class="abs cover-lead">OUR PURPOSE IS TO CREATE HIGH LEVEL<br>EXPERIENCES FOR OUR CLIENTS THROUGH</p>
    <h1 class="abs cover-title">DESIGN PLANNING</h1>
    <p class="abs cover-sub">CONSTRUCTION &amp; DEVELOPMENT</p>
    <p class="abs cover-web">www.harbisonprojgroup.example</p>
  </section>

  <!-- Why page -->
  <section class="page why">
    <svg class="page-art" viewBox="0 0 438 620" preserveAspectRatio="none" aria-hidden="true">
      <defs>
        <linearGradient id="whyPhoto" x1="0" y1="0" x2="0" y2="1">
          <stop offset="0" stop-color="#d8dde2"/><stop offset=".45" stop-color="#3b3c42"/><stop offset=".75" stop-color="#5c6a4a"/><stop offset="1" stop-color="#3f6a2c"/>
        </linearGradient>
      </defs>
      <path d="M270 0 L360 0 L430 80 Q400 125 350 100Z" fill="#8d8d8d"/>
      <path d="M360 0 L438 0 L438 105 Z" fill="#2a2a2a"/>
      <path d="M300 0 L330 0 L400 90 L380 110 Z" fill="#c9c9c9"/>
      <rect x="0" y="427" width="270" height="193" fill="url(#whyPhoto)" role="img" aria-label="Photo of a dark restaurant building with a glowing sign on a green lawn"/>
      <polygon points="170,620 340,400 438,400 438,620" fill="#2d2d2d"/>
      <path d="M300 470 Q340 380 380 400 L438 450 L438 620 L220 620Z" fill="#4a4a4a"/>
      <polygon points="230,620 438,360 438,620" fill="#b8242f" opacity=".9"/>
      <polygon points="380,430 438,355 438,500" fill="#f08f8f"/>
    </svg>
    <h2 class="abs why-head">Why Harbison<strong>BUILDING<br>MANAGEMENT?</strong>Simple.....</h2>
    <span class="abs why-rule"></span>

    <div class="abs point" style="left:14px;top:88px">
      <h3>COST SAVINGS:</h3>
      <p>If your concepts' annual project volume is between (1 – 15) projects, you could save money outsourcing, vs utilizing in-house CM's or PM's.</p>
      <p class="note"><span class="mark">a.</span> Why? When you compare the compensation package w/ all benefits of a qualified Project Manager with 5+ year of management experience, the per-project cost burden from Harbison, is potentially 20-30 % less.</p>
    </div>
    <div class="abs point" style="left:151px;top:88px">
      <h3>SPEED:</h3>
      <p>Most likely, we are going to have much more robust processes and systems in place managing multiple projects simultaneously, at a more dynamic pace.</p>
      <p class="note"><span class="mark">a.</span> Benefit to You? Projects will move through the life cycle more quickly, efficiently and successfully, with guaranteed outcomes.</p>
    </div>
    <div class="abs point" style="left:14px;top:160px">
      <h3>INTEGRITY:</h3>
      <p>Because we are outsourced, we will push information faster, and communicate at a much higher level than an internal resource</p>
      <p class="note"><span class="mark">a.</span> Why? Our value add, is your piece of mind and delivering results. We have a long term vision and strategy, and we are only as good as our last project. We have to keep delivering, while maintaining a high level experience to our customers so that we can thrive and grow.</p>
    </div>
    <div class="abs point" style="left:151px;top:160px">
      <h3>EXPERIENCE:</h3>
      <p>Put simply, our team has managed hundreds of projects from restaurant, retail, commercial, warehouse, and government / military logistics - nationwide, and overseas.</p>
      <p class="note"><span class="mark">a.</span> What does this mean to you? You get the benefit of "best practices" we've acquired from partnering with other industry leading concepts and organizations.</p>
    </div>
    <div class="abs point" style="left:14px;top:245px">
      <h3>TECHNOLOGY:</h3>
      <p>We utilize the latest project management software platforms to ensure high level collaboration, accountability and information transfer.</p>
      <p class="note"><span class="mark">a.</span> TaskFrame &nbsp;&nbsp; <span class="mark">b.</span> GridLedger</p>
    </div>
  </section>

  <!-- Contact page -->
  <section class="page contact">
    <svg class="page-art" viewBox="0 0 438 620" preserveAspectRatio="none" aria-hidden="true">
      <defs>
        <linearGradient id="contactPhoto" x1="0" y1="0" x2="0" y2="1">
          <stop offset="0" stop-color="#2a0506"/><stop offset=".35" stop-color="#8e0f14"/><stop offset=".6" stop-color="#c4161c"/><stop offset="1" stop-color="#6a0a0d"/>
        </linearGradient>
        <linearGradient id="aerialPhoto" x1="0" y1="0" x2="1" y2="1">
          <stop offset="0" stop-color="#4b5a42"/><stop offset=".5" stop-color="#2f3a3a"/><stop offset="1" stop-color="#3c3f46"/>
        </linearGradient>
      </defs>
      <rect width="438" height="620" fill="url(#contactPhoto)" role="img" aria-label="Red-toned photo of a restaurant patio structure among trees at dusk"/>
      <polygon points="270,0 438,0 438,170" fill="#1a0202" opacity=".6"/>
      <polygon points="438,258 438,620 135,620" fill="url(#aerialPhoto)" role="img" aria-label="Aerial evening photo of a lit restaurant courtyard and park"/>
      <polygon points="0,450 150,620 0,620" fill="#120202" opacity=".85"/>
      <polygon points="0,380 230,620 120,620 0,500" fill="#1e0304" opacity=".6"/>
    </svg>
    <h2 class="abs contact-title">CONTACT US TODAY</h2>
    <p class="abs contact-line" style="top:129px">
      <svg viewBox="0 0 20 20" fill="none" stroke="#fff" stroke-width="1.5"><circle cx="10" cy="10" r="8"/><path d="M2 10h16M10 2c-3 3-3 13 0 16M10 2c3 3 3 13 0 16"/></svg>
      www.harbisonprojgroup.example</p>
    <p class="abs contact-line" style="top:154px">
      <svg viewBox="0 0 20 20" fill="none" stroke="#fff" stroke-width="1.5"><path d="M5 2l3 4-2 2c1 3 3 5 6 6l2-2 4 3-2 3C8 18 2 12 2 4z"/></svg>
      214-555-0193</p>
    <p class="abs contact-line" style="top:177px">
      <svg viewBox="0 0 20 20" fill="none" stroke="#fff" stroke-width="1.5"><rect x="2" y="4" width="16" height="12"/><path d="M2 4l8 7 8-7"/></svg>
      info@harbisonprojgroup.example</p>
    <div class="abs brand"><span class="brand-mark" style="width:40px;height:40px"></span><span class="brand-name">HARBISON PROJECTS</span></div>
    <p class="abs follow">Follow me on: <span class="dot"></span></p>
  </section>

</main>
</body>
</html>
```